Law Firm Website

We are looking to update our old, tired and very flat website. We have someone who will code and host the site but we need some design inspiration. The website will consist of no more than 2/3 pages, possibly with pop-ups for information. We already have all the blurb. We would like something distinctive, clean and eye-catching, using the purple and white theme that we already use on our firm stationery. Examples uploaded. Current website URL is www.dunmorewillett.example.

Industry/Entity Type

Law Firm

```html
<!DOCTYPE html>
<html lang="en">
<head>
<meta charset="utf-8">
<title>Dunmore &amp; Willett Solicitors</title>
<link href="https://fonts.googleapis.com/css2?family=Fjalla+One&family=Noto+Serif&family=Open+Sans:wght@400;600&family=Arimo&display=swap" rel="stylesheet">
<style>
:root{
  --purple:#5d4889;
  --purple-bright:#5a2d9c;
  --purple-dark:#2e2438;
  --ink:#222;
  --grey:#666;
  --line:#d6d6da;
  --white:#fff;
}
*{margin:0;padding:0;box-sizing:border-box}
html,body{width:1200px;height:1060px;overflow:hidden}
body{position:relative;background:var(--white);font-family:"Open Sans",sans-serif;color:var(--ink)}
.abs{position:absolute}

.site-header{left:0;top:0;width:1200px;height:119px;background:linear-gradient(#fff,#f0f0f2);border-bottom:1px solid var(--line)}
.brand{left:143px;top:30px;font-family:"Noto Serif",serif;font-size:36px;color:var(--purple);white-space:nowrap}
.call{left:840px;top:12px;display:flex;align-items:center;gap:8px;color:#554f6a}
.call-label{font-family:"Fjalla One",sans-serif;font-size:29px;letter-spacing:.5px;padding-right:8px;border-right:1px solid #554f6a;line-height:38px}
.call-numbers{font-size:15px;line-height:22px;color:#333}
.main-nav{left:515px;top:82px;display:flex;height:37px}
.main-nav a{font-size:16px;color:#222;text-decoration:none;padding:8px 17px 0;border-left:1px solid #d0d0d4;letter-spacing:.3px;white-space:nowrap}
.main-nav a:first-child{border-left:none}

.hero{left:129px;top:131px;width:938px;height:211px;border:1px solid #cfcfd4;background:#fff;padding:7px}
.hero-inner{width:100%;height:100%;background:#f4f4f7;position:relative;overflow:hidden}
.hero-photo{left:0;top:0;width:311px;height:195px;background:linear-gradient(120deg,#c9c2bc,#9a8f88 45%,#e8e6ea)}
.hero-title{left:372px;top:58px;font-family:"Noto Serif",serif;font-size:36px;color:var(--purple);white-space:nowrap}
.hero-sub{left:372px;top:112px;font-family:"Noto Serif",serif;font-size:26px;color:#2a2a2a;white-space:nowrap}

.offer{left:0;top:355px;width:1200px;height:101px;background:var(--purple)}
.offer-title{left:142px;top:27px;font-family:"Fjalla One",sans-serif;color:#fff;font-size:27px;white-space:nowrap}
.offer-title b{font-weight:400;font-size:38px}
.offer-text{left:491px;top:32px;width:360px;font-family:Arimo,sans-serif;font-size:14px;line-height:16px;color:#e2dcef}
.offer-button{left:871px;top:29px;width:173px;height:44px;background:#fff;border-radius:6px;font-family:Arimo,sans-serif;font-size:21px;color:#555;text-align:center;line-height:44px;letter-spacing:.5px}
.offer-shadow{left:871px;top:71px}

.intro{left:0;top:456px;width:1200px;height:299px;background:linear-gradient(#e6e6ea,#fff 60px);border-top:2px solid #d6d6da}
.col-head{display:flex;align-items:center;gap:10px;font-size:21px;color:#222;white-space:nowrap}
.icon-circle{width:37px;height:37px;border-radius:50%;border:2px solid #c8c8cc;background:#ececef}
.about-text{left:130px;top:78px;width:245px;font-size:12.5px;line-height:16.5px}
.about-reg{left:130px;top:222px;width:240px;font-size:12.5px;line-height:15px}
.why-list{left:434px;top:82px;width:300px;list-style:none;font-size:13px;line-height:16px}
.why-list li{position:relative;padding-left:26px;margin-bottom:7px}
.why-list li::before{content:"";position:absolute;left:2px;top:3px;width:11px;height:11px;border-radius:50%;background:var(--purple)}
.why-list li::after{content:"";position:absolute;left:5px;top:6px;border-left:5px solid #fff;border-top:2.5px solid transparent;border-bottom:2.5px solid transparent}
.offices-intro{left:779px;top:75px;width:290px;font-size:13px;line-height:15px}
.office-rule{left:779px;top:117px;width:290px;border-top:1px solid #b8b8bc}
.office{left:782px;width:270px;display:flex;justify-content:space-between;align-items:center;font-size:15px}
.office span{font-size:11px;color:#666;display:flex;align-items:center;gap:10px}

.info{left:0;top:761px;width:1200px;height:238px;background:#fff;border-top:6px solid #ececef;border-bottom:3px solid #ececef}
.info h2{font-weight:400;font-size:21px;position:absolute;white-space:nowrap}
.services{font-size:12px;line-height:16.6px;color:#555;list-style:none;top:54px}
.bubble{left:495px;top:54px}
.quote{left:514px;top:64px;width:235px;font-style:italic;font-size:13px;line-height:15px;color:var(--purple)}
.quote-name{left:600px;top:178px;width:157px;text-align:right;font-style:italic;font-size:13px;color:var(--purple)}
.quote-place{left:600px;top:194px;width:157px;text-align:right;font-style:italic;font-size:13px}
.contact{font-size:12px;line-height:14.3px;color:#333;top:56px;white-space:nowrap}
.contact b{color:var(--purple-bright);font-weight:400}

.site-footer{left:0;top:1010px;width:1200px;height:50px;background:var(--purple-dark);color:#fff;font-size:12px;padding:16px 0 0 132px}
</style>
</head>
<body>

<header class="site-header abs">
  <div class="brand abs">Dunmore &amp; Willett</div>
  <div class="call abs">
    <div class="call-label">CALL US:</div>
    <div class="call-numbers">0333 555 0148<br>0845 555 0192</div>
  </div>
  <nav class="main-nav abs">
    <a href="#">HOME</a><a href="#">DANIEL DUNMORE</a><a href="#">PETER WILLETT</a><a href="#">EXPERTISE</a><a href="#">CONTACT</a>
  </nav>
</header>

<section class="hero abs">
  <div class="hero-inner">
    <div class="hero-photo abs" role="img" aria-label="Photo of a solicitor meeting two smiling clients at a table"></div>
    <div class="hero-title abs">Dunmore &amp; Willett Solicitors</div>
    <div class="hero-sub abs">For The Service You Deserve</div>
  </div>
</section>

<section class="offer abs">
  <div class="offer-title abs"><b>FREE</b> 30 Minute Consultation</div>
  <p class="offer-text abs">If you would like advice about your legal matter, we would offer you a free, no obligation, Half an hour appointment.</p>
  <svg class="offer-shadow abs" width="173" height="18" viewBox="0 0 173 18"><path d="M0 0 Q86 22 173 0 Q86 8 0 0Z" fill="#2e2438" opacity=".6"/></svg>
  <div class="offer-button abs">CONTACT US</div>
</section>

<section class="intro abs">
  <div class="col-head abs" style="left:129px;top:20px"><span class="icon-circle"></span>About us</div>
  <p class="about-text abs">Nam suscipit, risus ac convallis auctor, enim diam fermentum eros, ac semper diam felis imperdiet lorem. Nunc lobortis felis in dui ullamcorper eu imperdiet turpis luctus. Mauris vestibulum lacinia ligula, vel cursus elit interdum a. Aliquam fringilla ligula ac sapien scelerisque facilisis.</p>
  <p class="about-reg abs">This firm is authorised and regulated by the Solicitors Regulation Authority, no.600173</p>

  <div class="col-head abs" style="left:434px;top:20px"><span class="icon-circle"></span>Why Dunmore &amp; Willett</div>
  <ul class="why-list abs">
    <li>Be friendly, caring and polite in all our dealings with you</li>
    <li>Give you clear and practical legal advice</li>
    <li>Keep you updated throughout your case and ensure you understand when you can expect to hear from us</li>
    <li>Always work with your best interests in mind</li>
    <li>Represent you professionally throughout your case</li>
  </ul>

  <div class="col-head abs" style="left:779px;top:20px"><span class="icon-circle"></span>Our Offices</div>
  <p class="offices-intro abs">Click on your local office to find out about the specialist services we provide in your area:</p>
  <div class="office-rule abs"></div>
  <div class="office abs" style="top:131px">Hampstead<span>View Location <svg width="12" height="17" viewBox="0 0 12 17"><path d="M6 0a6 6 0 0 0-6 6c0 4.5 6 11 6 11s6-6.5 6-11a6 6 0 0 0-6-6z" fill="#aaa"/><circle cx="6" cy="6" r="2.3" fill="#fff"/></svg></span></div>
  <div class="office abs" style="top:164px">London<span>View Location <svg width="12" height="17" viewBox="0 0 12 17"><path d="M6 0a6 6 0 0 0-6 6c0 4.5 6 11 6 11s6-6.5 6-11a6 6 0 0 0-6-6z" fill="#aaa"/><circle cx="6" cy="6" r="2.3" fill="#fff"/></svg></span></div>
  <div class="office abs" style="top:197px">Welwyn<span>View Location <svg width="12" height="17" viewBox="0 0 12 17"><path d="M6 0a6 6 0 0 0-6 6c0 4.5 6 11 6 11s6-6.5 6-11a6 6 0 0 0-6-6z" fill="#aaa"/><circle cx="6" cy="6" r="2.3" fill="#fff"/></svg></span></div>
  <div class="office abs" style="top:230px">Hertfordshire<span>View Location <svg width="12" height="17" viewBox="0 0 12 17"><path d="M6 0a6 6 0 0 0-6 6c0 4.5 6 11 6 11s6-6.5 6-11a6 6 0 0 0-6-6z" fill="#aaa"/><circle cx="6" cy="6" r="2.3" fill="#fff"/></svg></span></div>
</section>

<section class="info abs">
  <h2 style="left:129px;top:16px">Our Services</h2>
  <ul class="services abs" style="left:136px">
    <li>Company Matters</li><li>Commercial Matters</li><li>Commercial Crime</li><li>Litigation/Disputes</li><li>Insolvency</li><li>Residential Conveyancing</li><li>Commercial Conveyancing</li><li>Wills &amp; Probate</li>
  </ul>
  <ul class="services abs" style="left:322px">
    <li>Estate Planning</li><li>Powers of Attorney</li><li>Care of the Elderly</li><li>Court of Protection</li><li>Divorce/Family</li><li>Pre-Nuptial Agreements</li><li>Intellectual Property</li><li>Media Law</li>
  </ul>

  <h2 style="left:499px;top:16px">Testimonials</h2>
  <svg class="bubble abs" width="272" height="114" viewBox="0 0 272 114"><path d="M10 .5h252a9.5 9.5 0 0 1 9.5 9.5v78a9.5 9.5 0 0 1-9.5 9.5h-42l-10 14-10-14H10A9.5 9.5 0 0 1 .5 88V10A9.5 9.5 0 0 1 10 .5z" fill="#fff" stroke="#c4c4c8"/></svg>
  <p class="quote abs">“Thank you, thank you, thank you. Your hard work and dedication has changed my life for the better”.</p>
  <div class="quote-name abs">Name here</div>
  <div class="quote-place abs">Dummy Place here</div>

  <h2 style="left:814px;top:16px">Contect Info</h2>
  <p class="contact abs" style="left:816px">Daniel Dunmore<br>12b Elmcroft Row<br>Hampstead<br>London NW3 9ZX<br><br><b>Tel:</b> 0333 555 0148<br><b>Fax:</b> 020 7946 0321</p>
  <p class="contact abs" style="left:950px">Peter Willett<br>41 Orchard Lane<br>Welwyn<br>Hertfordshire AL6 9QX<br><br><b>Tel:</b> 0845 555 0192<br><b>Fax:</b> 020 7946 0587</p>
</section>

<footer class="site-footer abs">Legal Notices | Privacy Policy | © Dunmore &amp; Willett</footer>

</body>
</html>
```